Postcard About Outsourcing Paperwork

Pemberton, Inc. help nonprofits register so that they can solicit contributions in various states so essentially we are a consulting company who handles paperwork for charities. I have uploaded our logo and a couple other images that we have on our website. We want an oversized post card which on the front says something like "Tired of signing your state registrations". On the back of the card, the right half the card will need name for addresses to print. the right will have spiel about us, but could also have images. The verbiage will be something like "Not only can we file your state registrations, but we can sign and notarize them, and can cut the checks for the state fees. Pemberton file tens of thousands of state registrations each year. Call us today at 760-555-0147 or email us at info@pembertoninc.example to see how we can help you. You can also visit our website at www.pembertoninc.example"

Target Market(s)

We are targeting Charities

Industry/Entity Type

It Company

Requirements
Nice to have
• Our logo(uploaded) and the color blue (matching our logo, website, letterhead) could be good to have

```html
<!DOCTYPE html>
<html lang="en">
<head>
<meta charset="utf-8">
<title>Pemberton, Inc. — State Registration Postcard</title>
<link rel="stylesheet" href="https://fonts.googleapis.com/css2?family=Kreon:wght@400;500;600;700&family=Open+Sans:wght@400;600;700&display=swap">
<style>
  :root {
    --backdrop: #cfd1d3;
    --paper: #ffffff;
    --brand-blue: #1a56b0;
    --brand-blue-deep: #0e3f93;
    --ink: #222222;
  }
  * { box-sizing: border-box; margin: 0; padding: 0; }
  html, body { width: 936px; height: 1200px; overflow: hidden; background: var(--backdrop); }
  body { position: relative; font-family: "Kreon", Georgia, serif; color: var(--ink); }

  .card {
    position: absolute; left: 48px; width: 840px; height: 544px;
    background: var(--paper); overflow: hidden;
    box-shadow: 0 3px 10px rgba(0,0,0,.25);
  }
  .card--front { top: 36px; }
  .card--back { top: 620px; }

  /* Front */
  .front-band {
    position: absolute; left: 0; top: 0; width: 100%; height: 122px;
    background: linear-gradient(90deg, #1552b4 0%, #2461c0 65%, #8ea9d6 85%, #c9d3e3 100%);
  }
  .front-question {
    position: absolute; left: 32px; top: 66px; line-height: 1.2;
    font-size: 27px; font-weight: 600; color: #fff; letter-spacing: .2px;
  }
  .front-photo {
    position: absolute; left: 0; top: 122px; width: 100%; height: 324px;
    background: linear-gradient(160deg, #f4f5f6 0%, #d9dcdf 40%, #eceef0 70%, #ffffff 100%);
  }
  .front-headline {
    position: absolute; right: 34px; top: 134px; line-height: 1.2;
    font-size: 56px; font-weight: 600; color: var(--brand-blue); letter-spacing: -.3px;
  }
  .front-footer {
    position: absolute; left: 0; top: 446px; width: 100%; height: 98px; background: var(--paper);
  }
  .front-contact { position: absolute; right: 26px; top: 20px; text-align: right; }
  .front-phone {
    font-family: "Open Sans", Arial, sans-serif; font-weight: 600;
    font-size: 30px; color: var(--brand-blue); line-height: 36px;
  }
  .front-url {
    margin-top: 4px; font-family: "Open Sans", Arial, sans-serif; font-weight: 700;
    font-size: 18px; line-height: 22px; color: var(--ink);
  }

  /* Brand signature */
  .brand { position: absolute; display: flex; align-items: center; gap: 10px; }
  .brand-mark { width: 44px; height: 44px; background: var(--brand-blue); flex: none; }
  .brand-name { font-size: 25px; font-weight: 500; color: var(--brand-blue); line-height: 1.2; }
  .front-footer .brand { left: 30px; top: 26px; }

  /* Back */
  .back-forms {
    position: absolute; left: 0; top: 0; width: 364px; height: 76px;
    background: linear-gradient(180deg, #e9ebee 0%, #ffffff 100%);
  }
  .back-copy {
    position: absolute; left: 30px; top: 79px; width: 494px; z-index: 2;
    font-size: 13.2px; line-height: 18.6px; color: var(--ink);
  }
  .copy-notch { float: right; width: 150px; height: 149px; }
  .drop-cap {
    float: left; font-size: 64px; line-height: 52px; font-weight: 700;
    color: var(--brand-blue-deep); margin: 3px 6px 0 0;
  }
  .back-maze {
    position: absolute; left: 0; top: 388px; width: 560px; height: 156px;
    background: linear-gradient(180deg, #ffffff 0%, #e3e5e8 45%, #d2d5d9 100%);
  }
  .address-panel {
    position: absolute; left: 364px; top: 474px; width: 196px; height: 70px; background: var(--paper);
  }
  .back-cta { position: absolute; left: 30px; top: 362px; z-index: 2; }
  .back-cta-line { font-size: 17px; font-weight: 600; color: var(--ink); line-height: 22px; }
  .back-cta-phone {
    margin-top: 4px; font-family: "Open Sans", Arial, sans-serif; font-weight: 600;
    font-size: 30px; color: var(--brand-blue); line-height: 36px;
  }
  .back-card-info { position: absolute; left: 404px; top: 24px; z-index: 2; }
  .back-card-info .brand { position: static; }
  .back-card-info .brand-mark { width: 52px; height: 52px; }
  .offices {
    display: flex; margin-top: 24px;
    font-family: "Open Sans", Arial, sans-serif; font-size: 11px; line-height: 14px; color: var(--brand-blue);
  }
  .office { font-style: normal; }
  .office--east { width: 129px; }
  .office-contacts {
    margin-top: 14px; font-family: "Open Sans", Arial, sans-serif;
    font-size: 11px; line-height: 14px; color: var(--brand-blue);
  }
  .office-contacts .phone { font-weight: 700; }
</style>
</head>
<body>

<section class="card card--front">
  <div class="front-band" role="img" aria-label="Blue-tinted photo of tax and registration forms"></div>
  <h1 class="front-question">Tired of signing your state registrations?</h1>
  <div class="front-photo" role="img" aria-label="Photo of a businessman standing inside a white maze"></div>
  <h2 class="front-headline">We can help you.</h2>
  <div class="front-footer">
    <div class="brand">
      <span class="brand-mark"></span>
      <span class="brand-name">Pemberton, Inc.</span>
    </div>
    <div class="front-contact">
      <div class="front-phone">(760) 555-0147</div>
      <div class="front-url">www.pembertoninc.example</div>
    </div>
  </div>
</section>

<section class="card card--back">
  <div class="back-forms" role="img" aria-label="Faded photo of tax and registration forms"></div>
  <p class="back-copy"><span class="copy-notch"></span><span class="drop-cap">F</span>or more a quarter century we have been assisting charities, fundraisers and solicitors with registering and remaining in compliance with state regulations. We prepare all the necessary forms and attachments, correspond with the states, set up registered agents, do your extensions and make the process easy for you. We have hundreds of satisfied clients and we can help you too. We are the state registration professionals and state registrations are the only thing we do so you can be assured that we can get you registered and keep you registered. We figure out which specific requirements affect your organization and what steps you need to take. We provide annual state registration services, registrations for charitable gift annuities and registration for inclusion in state employee campaigns.</p>
  <div class="back-maze" role="img" aria-label="Faded photo of a white maze seen from above"></div>
  <div class="address-panel"></div>
  <div class="back-cta">
    <div class="back-cta-line">Contact us today to see how we can help you!</div>
    <div class="back-cta-phone">(760) 555-0147</div>
  </div>

  <div class="back-card-info">
    <div class="brand">
      <span class="brand-mark"></span>
      <span class="brand-name">Pemberton, Inc.</span>
    </div>
    <div class="offices">
      <address class="office office--east">East Coast Office<br>2240 Harbor Mill Road<br>Annapolis, MD 21401</address>
      <address class="office office--west">West Coast Office<br>415 Cedar Crest Way, Suite 120<br>Oceanside, CA 92054</address>
    </div>
    <div class="office-contacts">
      <div class="phone">(760) 555-0147</div>
      <div>info@pembertoninc.example</div>
      <div>www.pembertoninc.example</div>
    </div>
  </div>
</section>

</body>
</html>
```